Figma App design and working prototype

I need to create a User Interface design and a Working prototype using Figma or similar. I’d also like all the assets and guidelines needed to guide the App developers to create the final product.
So, I'll need Design files and assets but you that I can give to an App development company or a freelance developer to create Android and iOS apps.

This app is an app for adults who wan to meet and have sex no strings attached.

The App name will be Nuvora

I have attached an app some pictures and a pdf file explaining details of the apps functions.

This app will be a sexy version of the pobalo app with a personals section used for adult services. I have attached images and a pdf below that will tell you the functions of the app.

I need an app interface design done for an app idea I have. I am nee to this it is my first time trying to launch an app and I do not know what you need in order to get what I need. I need a site map/ design and if possible a working prototype that I can pass on to an app developer that can deliver the final product. This model will be used to raise funds and give investors an idea of what the apps functions will do as detailed in the project brief. Any advise would be greatly appreciated. Please let me know if you have any questions. Looking forward to working with you.

Target Market(s)

Adults men and women looking for some adult entertainment

Industry/Entity Type

Adult entertainment Strip clubs

Colors
E54698
E96AAD
F1A4CE
F9D9EA
FCEFF6
A7469A
B969AE
D3A5CF
EDDBEB
F8F0F9
6B429C
8869AF
B7A5CE
E3DAEB
F3F0F8

Requirements
Must have
• An 18+ confirmation,
Nice to have
• A sexy feel.

```html
<!DOCTYPE html>
<html lang="en">
<head>
<meta charset="utf-8">
<title>Nuvora – Home Screen</title>
<link href="https://fonts.googleapis.com/css2?family=Poppins:wght@400;500;600;700&display=swap" rel="stylesheet">
<style>
  :root{
    --pink:#E54698;
    --pink-soft:#E96AAD;
    --magenta:#A7469A;
    --violet:#6B429C;
    --violet-mid:#8869AF;
    --lilac:#D3A5CF;
    --blush:#F9D9EA;
    --mist:#F3F0F8;
    --ink:#1c1524;
    --grey:#6d6a72;
    --field:#eeedf0;
    --verified:#3b8ee8;
    --white:#ffffff;
  }
  *{box-sizing:border-box;margin:0;padding:0}
  html,body{width:1200px;height:864px;overflow:hidden}
  body{position:relative;background:var(--white);font-family:"Poppins",sans-serif;color:var(--ink)}

  .backdrop-blob{position:absolute;border-radius:50%}
  .blob-top{width:760px;height:520px;left:-220px;top:-330px;background:linear-gradient(120deg,var(--blush),var(--lilac) 55%,var(--violet-mid));opacity:.8}
  .blob-bottom{width:700px;height:400px;right:-200px;bottom:-280px;background:linear-gradient(160deg,var(--blush),var(--pink-soft));opacity:.7}

  .brand{position:absolute;left:70px;top:380px;display:flex;align-items:center;gap:16px}
  .brand-dot{width:34px;height:34px;border-radius:50%;background:var(--pink)}
  .brand-name{font-size:64px;font-weight:500;color:var(--pink);letter-spacing:1px;line-height:1}

  .screen{position:absolute;left:810px;top:22px;width:330px;height:820px;background:var(--white);border-radius:34px;overflow:hidden;box-shadow:0 0 0 7px #141216,0 18px 40px rgba(60,30,90,.25)}

  .status{position:absolute;left:0;top:0;width:100%;height:44px;display:flex;justify-content:space-between;align-items:center;padding:10px 26px 0}
  .status-time{font-size:14px;font-weight:600}
  .status-icons{display:flex;gap:5px;align-items:center}

  .search{position:absolute;left:18px;top:58px;width:248px;height:30px;border-radius:8px;background:var(--field);display:flex;align-items:center;gap:8px;padding-left:10px;font-size:12px;color:var(--violet)}
  .bell{position:absolute;left:280px;top:60px}
  .badge{position:absolute;left:292px;top:55px;width:16px;height:16px;border-radius:50%;background:#e8303a;color:var(--white);font-size:9px;font-weight:600;display:flex;align-items:center;justify-content:center}

  .stories{position:absolute;left:16px;top:100px;display:flex;gap:20px}
  .story{width:48px;text-align:center;font-size:8.5px;font-weight:500}
  .story-avatar{width:48px;height:48px;border-radius:50%;background:linear-gradient(150deg,#c9a38a,#7c4d3c);margin-bottom:7px}

  .featured{position:absolute;left:0;top:176px;width:100%;height:124px;background:linear-gradient(100deg,#8a2d8e,#5a2c8e 60%,#3f2a86)}
  .featured-photo{position:absolute;left:14px;top:12px;width:146px;height:86px;border-radius:6px;border:2px solid var(--pink);background:linear-gradient(130deg,#8a7430,#c08a66 55%,#5a4030)}
  .featured-tag{position:absolute;left:100px;top:12px;height:16px;padding:0 7px 0 4px;border-radius:8px;background:#2a1a2e;color:var(--pink);font-size:7.5px;font-weight:600;display:flex;align-items:center;gap:4px}
  .featured-name{position:absolute;left:180px;top:16px;color:var(--white);font-size:15px;font-weight:600;display:flex;align-items:center;gap:5px}
  .featured-city{position:absolute;left:180px;top:40px;color:#e9dff0;font-size:9px}
  .book-btn{position:absolute;left:180px;top:64px;width:114px;height:28px;border-radius:14px;background:var(--white);color:var(--pink);font-size:10.5px;font-weight:600;display:flex;align-items:center;justify-content:center;gap:8px}
  .dots{position:absolute;left:105px;top:108px;display:flex;gap:5px;align-items:center}
  .dots span{width:4px;height:4px;border-radius:50%;background:var(--white)}
  .dots .dot-active{width:24px;border-radius:2px}

  .categories{position:absolute;left:12px;top:314px;width:306px;height:110px;border-radius:10px;background:var(--white);box-shadow:0 2px 10px rgba(40,20,60,.1)}
  .section-title{position:absolute;left:12px;top:10px;font-size:12.5px;font-weight:600}
  .see-all{position:absolute;right:12px;top:13px;font-size:9.5px;font-weight:600;color:var(--pink)}
  .cat-list{position:absolute;left:6px;top:40px;display:flex}
  .cat{width:74px;text-align:center;font-size:7.5px;font-weight:500}
  .cat-icon{width:40px;height:40px;border-radius:12px;margin:0 auto 10px;display:flex;align-items:center;justify-content:center}
  .cat-vip{background:linear-gradient(150deg,#c44fa4,#8a2d8e)}
  .cat-female{background:linear-gradient(150deg,#f06aa6,#e23b86)}
  .cat-male{background:linear-gradient(150deg,#2a8cf0,#1a5ed8)}
  .cat-strip{background:linear-gradient(150deg,#b05ce6,#7a36d6)}

  .nearby-kicker{position:absolute;left:14px;top:440px;font-size:8.5px;color:var(--grey);letter-spacing:.3px}
  .nearby-title{position:absolute;left:14px;top:452px;font-size:14.5px;font-weight:600}

  .card{position:absolute;width:136px;border-radius:8px;background:var(--white);box-shadow:0 2px 8px rgba(40,20,60,.1);overflow:hidden}
  .card-name{height:22px;display:flex;align-items:center;gap:4px;padding-left:8px;font-size:8.5px;font-weight:600}
  .card-photo{height:136px}
  .photo-warm{background:linear-gradient(150deg,#9a6d55,#c99a7e 50%,#6a4a3c)}
  .photo-shore{background:linear-gradient(150deg,#9a9a92,#d4c6b8 50%,#6e6a66)}
  .photo-sea{background:linear-gradient(180deg,#7fa3b8,#c9d8de 60%,#3c3430)}
  .photo-room{background:linear-gradient(160deg,#5e4a3e,#b89a84)}
  .card-meta{position:relative;padding:6px 8px 8px;font-size:8px;color:var(--grey)}
  .card-price{font-size:9.5px;font-weight:700;color:var(--ink);margin-top:2px}
  .card-heart{position:absolute;right:9px;top:10px}
  .vip-flag{position:absolute;right:0;top:0;width:20px;height:28px;background:var(--magenta);color:var(--white);font-size:5.5px;font-weight:600;text-align:center;padding-top:2px;clip-path:polygon(0 0,100% 0,100% 100%,50% 82%,0 100%)}

  .tabbar{position:absolute;left:0;bottom:0;width:100%;height:76px;background:var(--violet);display:flex;justify-content:space-around;padding-top:10px}
  .tab{width:58px;text-align:center;font-size:7.5px;color:#c9bedc;white-space:nowrap}
  .tab svg{display:block;margin:0 auto 3px}
  .tab-active{color:var(--white);font-weight:600}
  .home-bar{position:absolute;left:100px;bottom:8px;width:108px;height:4px;border-radius:2px;background:var(--white)}
</style>
</head>
<body>
  <div class="backdrop-blob blob-top"></div>
  <div class="backdrop-blob blob-bottom"></div>

  <div class="brand">
    <span class="brand-dot"></span>
    <span class="brand-name">Nuvora</span>
  </div>

  <main class="screen">
    <div class="status">
      <span class="status-time">9:41</span>
      <span class="status-icons">
        <svg width="16" height="10" viewBox="0 0 16 10"><rect x="0" y="7" width="3" height="3" fill="#000"/><rect x="4" y="5" width="3" height="5" fill="#000"/><rect x="8" y="3" width="3" height="7" fill="#000"/><rect x="12" y="0" width="3" height="10" fill="#000"/></svg>
        <svg width="14" height="10" viewBox="0 0 14 10"><path d="M1 3.5a9 9 0 0 1 12 0M3 5.8a6 6 0 0 1 8 0M5 8a3 3 0 0 1 4 0" stroke="#000" stroke-width="1.6" fill="none"/></svg>
        <svg width="22" height="11" viewBox="0 0 22 11"><rect x="0.5" y="0.5" width="19" height="10" rx="2.5" fill="none" stroke="#000"/><rect x="2" y="2" width="16" height="7" rx="1.5" fill="#000"/></svg>
      </span>
    </div>

    <div class="search">
      <svg width="13" height="13" viewBox="0 0 13 13"><circle cx="5.5" cy="5.5" r="4.3" stroke="#6B429C" stroke-width="1.6" fill="none"/><path d="M8.8 8.8 12 12" stroke="#6B429C" stroke-width="1.6"/></svg>
      Search
    </div>
    <svg class="bell" width="20" height="22" viewBox="0 0 20 22"><path d="M4 15V9a6 6 0 0 1 12 0v6l2 2H2z" fill="none" stroke="#1c1524" stroke-width="1.6" stroke-linejoin="round"/><path d="M8 19a2 2 0 0 0 4 0" fill="none" stroke="#1c1524" stroke-width="1.6"/></svg>
    <span class="badge">8</span>

    <div class="stories">
      <div class="story"><div class="story-avatar" role="img" aria-label="Profile photo of Megan"></div>Megan</div>
      <div class="story"><div class="story-avatar" role="img" aria-label="Profile photo of Audrey"></div>Audrey</div>
      <div class="story"><div class="story-avatar" role="img" aria-label="Profile photo of Alodia"></div>Alodia</div>
      <div class="story"><div class="story-avatar" role="img" aria-label="Profile photo of Yvonne"></div>Yvonne</div>
      <div class="story"><div class="story-avatar" role="img" aria-label="Profile photo of Chris"></div>Chris</div>
    </div>

    <section class="featured">
      <div class="featured-photo" role="img" aria-label="Featured profile photo of Katherine"></div>
      <span class="featured-tag">
        <svg width="10" height="10" viewBox="0 0 10 10"><circle cx="5" cy="5" r="5" fill="#E54698"/><path d="M5 2l.9 1.9 2 .2-1.5 1.4.4 2L5 6.5 3.2 7.5l.4-2L2.1 4.1l2-.2z" fill="#2a1a2e"/></svg>
        FEATURED
      </span>
      <div class="featured-name">Katherine
        <svg width="12" height="12" viewBox="0 0 12 12"><circle cx="6" cy="6" r="6" fill="#3b8ee8"/><path d="M3.3 6.2 5.2 8 8.8 4.3" stroke="#fff" stroke-width="1.5" fill="none"/></svg>
      </div>
      <div class="featured-city">Montreal, QC</div>
      <div class="book-btn">
        <svg width="13" height="13" viewBox="0 0 13 13"><rect x="1" y="2" width="11" height="10" rx="2" fill="none" stroke="#E54698" stroke-width="1.3"/><path d="M1 5h11M4 1v2M9 1v2" stroke="#E54698" stroke-width="1.3"/><circle cx="4" cy="8" r=".8" fill="#E54698"/><circle cx="6.5" cy="8" r=".8" fill="#E54698"/><circle cx="9" cy="8" r=".8" fill="#E54698"/></svg>
        Book Now
      </div>
      <div class="dots"><span class="dot-active"></span><span></span><span></span><span></span><span></span><span></span></div>
    </section>

    <section class="categories">
      <h2 class="section-title">Categories</h2>
      <span class="see-all">SEE ALL</span>
      <div class="cat-list">
        <div class="cat"><div class="cat-icon cat-vip"><svg width="18" height="18" viewBox="0 0 18 18"><path d="M9 2c0 3-4 5-4 9a4 4 0 0 0 8 0c0-2-1-3-2-4 0 2-1 3-2 3" fill="none" stroke="#fff" stroke-width="1.5" stroke-linejoin="round"/></svg></div>VIP Escorts</div>
        <div class="cat"><div class="cat-icon cat-female"><svg width="18" height="18" viewBox="0 0 18 18"><path d="M3 15V9a6 6 0 0 1 12 0v6M6 12a3 3 0 0 1 6 0" fill="none" stroke="#fff" stroke-width="1.5"/></svg></div>Female Escorts</div>
        <div class="cat"><div class="cat-icon cat-male"><svg width="18" height="18" viewBox="0 0 18 18"><path d="M5 8a4 4 0 0 1 8 0v2a4 4 0 0 1-8 0zM7 16h4" fill="none" stroke="#fff" stroke-width="1.5"/></svg></div>Male Escorts</div>
        <div class="cat"><div class="cat-icon cat-strip"><svg width="18" height="18" viewBox="0 0 18 18"><circle cx="11" cy="3.5" r="1.6" fill="#fff"/><path d="M10 6 7 11l3 5M10 6l3 3M7 11l-3 1M9 2v14" fill="none" stroke="#fff" stroke-width="1.5" stroke-linecap="round"/></svg></div>Strippers</div>
      </div>
    </section>

    <p class="nearby-kicker">ESCORTS NEARBY</p>
    <h2 class="nearby-title">Daily Discover</h2>

    <article class="card" style="left:12px;top:480px">
      <div class="card-name">Ashley <svg width="9" height="9" viewBox="0 0 12 12"><circle cx="6" cy="6" r="6" fill="#3b8ee8"/><path d="M3.3 6.2 5.2 8 8.8 4.3" stroke="#fff" stroke-width="1.5" fill="none"/></svg></div>
      <div class="card-photo photo-warm" role="img" aria-label="Profile photo of Ashley"></div>
      <div class="card-meta">Montreal, QC<div class="card-price">$300/h</div>
        <svg class="card-heart" width="16" height="14" viewBox="0 0 16 14"><path d="M8 13 1.8 7A3.6 3.6 0 0 1 8 2.3 3.6 3.6 0 0 1 14.2 7z" fill="#E54698"/></svg>
      </div>
    </article>
    <article class="card" style="left:170px;top:480px">
      <div class="card-name">Cassandra <svg width="9" height="9" viewBox="0 0 12 12"><circle cx="6" cy="6" r="6" fill="#3b8ee8"/><path d="M3.3 6.2 5.2 8 8.8 4.3" stroke="#fff" stroke-width="1.5" fill="none"/></svg></div>
      <span class="vip-flag">VIP</span>
      <div class="card-photo photo-shore" role="img" aria-label="Profile photo of Cassandra"></div>
      <div class="card-meta">Montreal, QC<div class="card-price">$300/h</div>
        <svg class="card-heart" width="16" height="14" viewBox="0 0 16 14"><path d="M8 13 1.8 7A3.6 3.6 0 0 1 8 2.3 3.6 3.6 0 0 1 14.2 7z" fill="none" stroke="#1c1524" stroke-width="1.4"/></svg>
      </div>
    </article>
    <article class="card" style="left:12px;top:690px">
      <div class="card-name">Vanessa <svg width="9" height="9" viewBox="0 0 12 12"><circle cx="6" cy="6" r="6" fill="#3b8ee8"/><path d="M3.3 6.2 5.2 8 8.8 4.3" stroke="#fff" stroke-width="1.5" fill="none"/></svg></div>
      <span class="vip-flag">VIP</span>
      <div class="card-photo photo-sea" role="img" aria-label="Profile photo of Vanessa"></div>
    </article>
    <article class="card" style="left:170px;top:690px">
      <div class="card-name">Stephanie <svg width="9" height="9" viewBox="0 0 12 12"><circle cx="6" cy="6" r="6" fill="#3b8ee8"/><path d="M3.3 6.2 5.2 8 8.8 4.3" stroke="#fff" stroke-width="1.5" fill="none"/></svg></div>
      <div class="card-photo photo-room" role="img" aria-label="Profile photo of Stephanie"></div>
    </article>

    <nav class="tabbar">
      <div class="tab tab-active"><svg width="18" height="18" viewBox="0 0 18 18"><rect x="2" y="2" width="14" height="5" rx="1.5" fill="none" stroke="#fff" stroke-width="1.5"/><rect x="2" y="10" width="6" height="6" rx="1.5" fill="none" stroke="#fff" stroke-width="1.5"/><rect x="10" y="10" width="6" height="6" rx="1.5" fill="none" stroke="#fff" stroke-width="1.5"/></svg>Home</div>
      <div class="tab"><svg width="18" height="18" viewBox="0 0 18 18"><path d="M2 3h14v9H7l-4 3v-3H2z" fill="none" stroke="#c9bedc" stroke-width="1.4" stroke-linejoin="round"/><path d="M5 6h8M5 9h5" stroke="#c9bedc" stroke-width="1.4"/></svg>Messagaes</div>
      <div class="tab"><svg width="18" height="18" viewBox="0 0 18 18"><rect x="2" y="2" width="14" height="14" rx="2" fill="none" stroke="#c9bedc" stroke-width="1.4"/><path d="M9 5v8M5 9h8" stroke="#c9bedc" stroke-width="1.4"/></svg>Post</div>
      <div class="tab"><svg width="18" height="18" viewBox="0 0 16 14"><path d="M8 13 1.8 7A3.6 3.6 0 0 1 8 2.3 3.6 3.6 0 0 1 14.2 7z" fill="none" stroke="#c9bedc" stroke-width="1.2"/></svg>Favourites</div>
      <div class="tab"><svg width="18" height="18" viewBox="0 0 18 18"><circle cx="9" cy="6" r="3.3" fill="none" stroke="#c9bedc" stroke-width="1.4"/><path d="M3 16a6 6 0 0 1 12 0" fill="none" stroke="#c9bedc" stroke-width="1.4"/></svg>My Velvet</div>
      <span class="home-bar"></span>
    </nav>
  </main>
</body>
</html>
```